Hack my website! Blue Harbor needs a site

We hack stuff. No joke, that is what we do, but we are the good guys!

We do security consulting, specifically offensive security. The technical term is "Penetration Testing", but you probably know it as "hacking". Companies hire us to break in before the bad guys do. (I have a very cool job :) ).

I need a web site to describe our offerings and connect with clients.

I've included my business card and logo so you can understand what I'm looking for on the website and the color scheme.

Tag line:
Offensive Services from Offensive Minds

Target Market(s)

Medium to large businesses

Industry/Entity Type

Computer Security

Coding

Coded - Design and coding required

Number of Pages Required

2 page

Font styles to use
Sans Serif

Colors

Designer to choose colors to be used in the design.

Requirements
Must have
• Flat, clean, professional look
Nice to have
• Bonus for bootstrap. See the uploaded logo for the current colors. I'd really like this to look decent on a phone too.
Should not have
• 1. Black background
• 2. The business card is to show the colors and theme so far. Please, do NOT just slam that into the middle of the site since it doesn't make sense. It feels odd that I have to say that, but I've received multiple submissions where people have done this.

```html
<!DOCTYPE html>
<html lang="en">
<head>
<meta charset="utf-8">
<title>Blue Harbor — Offensive Solutions from Offensive Minds</title>
<link rel="stylesheet" href="https://fonts.googleapis.com/css2?family=Arimo:wght@400;700&display=swap">
<style>
:root{
  --red:#d0141c;
  --red-deep:#c20f17;
  --red-soft:#e0767b;
  --ink:#111111;
  --charcoal:#353535;
  --slate:#9a9a9a;
  --white:#ffffff;
  --muted:#b7b7b7;
  --field:#c8c8c8;
}
*{margin:0;padding:0;box-sizing:border-box}
html,body{width:1200px;height:4036px;overflow:hidden}
body{font-family:"Arimo",Arial,sans-serif;color:var(--white);position:relative;background:var(--white)}
section,header,footer{position:absolute;left:0;width:1200px;overflow:hidden}
.abs{position:absolute}
.brand{display:flex;align-items:center;gap:14px;font-weight:700;letter-spacing:6px;text-transform:uppercase}
.brand-mark{width:30px;height:30px;background:var(--red)}
.red{color:var(--red)}

/* hero */
.hero{top:0;height:599px;background:radial-gradient(ellipse at 70% 40%,#474747 0%,#333 55%,#2b2b2b 100%)}
.hero .brand{left:75px;top:30px;font-size:22px}
.nav{left:755px;top:40px;display:flex;gap:16px;font-size:22px}
.rule{height:2px;background:#8a8a8a}
.hero-title{left:75px;top:345px;font-size:66px;font-weight:700;line-height:78px;text-transform:uppercase}
.vline{left:1072px;top:121px;width:2px;height:405px;background:#bfbfbf}
.vdot{left:1064px;top:113px;width:18px;height:18px;border-radius:50%;background:var(--white)}
.vlabel{left:1048px;top:430px;font-size:13px;transform:rotate(-90deg);transform-origin:left top;letter-spacing:1px;color:#ddd}
.info{left:963px;top:520px;font-size:13px;font-weight:700}

/* what we do */
.about-intro{top:599px;height:386px;background:linear-gradient(90deg,#a6a6a6 0%,#9a9a9a 70%,#8e8e8e 100%)}
.section-title{font-size:58px;font-weight:700;text-transform:uppercase}
.about-intro .section-title{left:75px;top:60px}
.lead{left:75px;top:150px;font-size:24px;font-weight:700}
.intro-text{left:75px;top:193px;width:720px;font-size:20px;line-height:26px;font-weight:700}
.intro-brand{left:890px;top:160px;flex-direction:column;gap:18px;font-size:24px;letter-spacing:4px;color:var(--red)}
.intro-brand .brand-mark{width:120px;height:120px}

/* services */
.services{top:985px;height:1108px;background:var(--red)}
.services .section-title{left:75px;top:65px}
.services-sub{left:75px;top:150px;font-size:19px;font-weight:700}
.service-grid{left:75px;top:255px;width:1050px;display:grid;grid-template-columns:repeat(3,1fr);grid-template-rows:418px 380px;row-gap:20px}
.service{padding:0 22px 0 0}
.service:nth-child(3n+2),.service:nth-child(3n){padding-left:20px;border-left:2px solid rgba(255,255,255,.55)}
.service-icon{display:block;margin:0 auto 14px auto;width:56px;height:56px}
.service h3{font-size:21px;line-height:24px;margin-bottom:14px}
.service p{font-size:17px;line-height:21px;font-weight:700}

/* about */
.about{top:2093px;height:510px;background:#050505}
.about-shade{left:0;top:0;width:1200px;height:510px}
.about .section-title{left:75px;top:85px;font-size:60px}
.about-text{left:75px;top:155px;width:400px;font-size:20px;line-height:24px;font-weight:700}
.device{left:485px;top:27px;width:642px;height:474px;border-radius:14px;background:linear-gradient(160deg,#5a5a5a 0%,#2e2e2e 60%,#1b1b1b 100%)}

/* contact */
.contact{top:2603px;height:553px;background:var(--white);color:var(--ink)}
.contact .section-title{left:75px;top:80px}
.contact-sub{left:78px;top:150px;font-size:21px;line-height:26px;color:var(--red)}
.field{height:79px;border:3px solid #222;font-size:23px;color:var(--field);padding:0 28px;display:flex;align-items:center;text-transform:uppercase;letter-spacing:1px}
.send{left:715px;top:455px;width:170px;height:54px;border:3px solid #222;color:var(--red);font-weight:700;font-size:24px;display:flex;align-items:center;justify-content:center}

/* testimonial */
.testimonial{top:3156px;height:458px;background:var(--red-deep);text-align:center}
.quote{top:20px;font-size:300px;font-weight:700;color:#d9585e;line-height:1}
.avatar{left:524px;top:65px;width:150px;height:150px;border-radius:50%;background:radial-gradient(circle at 50% 40%,#b9a59a 0%,#5b4e48 70%,#3a3431 100%)}
.cite{left:0;top:232px;width:1200px;font-size:25px}
.quote-text{left:155px;top:273px;width:890px;font-size:20px;line-height:26px;font-weight:700}
.arrow{top:207px;width:86px;height:70px;background:var(--red-soft);display:flex;align-items:center;justify-content:center}

/* footer */
.site-footer{top:3614px;height:422px;background:#0b0b0b}
.site-footer .brand{left:75px;top:100px;font-size:30px;color:var(--red)}
.footer-tag{left:75px;top:160px;font-size:18px;font-weight:700;line-height:22px}
.footer-text{left:75px;top:210px;width:330px;font-size:19px;line-height:24px;font-weight:700}
.footer-head{font-size:31px}
.social{left:531px;top:150px;display:flex;gap:26px}
.social span{width:34px;height:34px;background:var(--white);border-radius:4px}
.contact-line{left:531px;display:flex;align-items:center;gap:22px;font-size:23px}
.links{left:863px;top:158px;list-style:none;font-size:24px;font-weight:700;line-height:33px}
.links li::before{content:"";display:inline-block;width:10px;height:10px;border-radius:50%;background:var(--red);margin-right:18px;vertical-align:middle}
.copyright{left:0;top:372px;width:1200px;height:50px;border-top:2px solid #444;display:flex;align-items:center;justify-content:center;font-size:21px;font-weight:700}
</style>
</head>
<body>

<header class="hero">
  <div class="abs brand"><span class="brand-mark"></span>Blue Harbor</div>
  <nav class="abs nav"><span>HOME</span><span>ABOUT US</span><span>CONTACT</span></nav>
  <div class="abs rule" style="left:75px;top:97px;width:613px"></div>
  <div class="abs rule" style="left:758px;top:97px;width:335px"></div>
  <div class="abs vline"></div>
  <div class="abs vdot"></div>
  <div class="abs vlabel">SECURITY</div>
  <div class="abs info">INFORMATION</div>
  <h1 class="abs hero-title"><span class="red">Offensive</span> Solutions<br>from <span class="red">Offensive</span> Minds</h1>
</header>

<section class="about-intro">
  <h2 class="abs section-title">What we do?</h2>
  <p class="abs lead">We hack stuff. No joke, that is what we do, but we are the good guys!</p>
  <p class="abs intro-text">We do security consulting, specifically offensive security. The technical term is "Penetration Testing", but you probably know it as "hacking". Companies hire us to break in before the bad guys do.</p>
  <div class="abs brand intro-brand"><span class="brand-mark"></span>Blue Harbor</div>
</section>

<section class="services">
  <h2 class="abs section-title">Services</h2>
  <p class="abs services-sub">These are all the services that we are providing to our costumers.</p>
  <div class="abs service-grid">
    <article class="service">
      <svg class="service-icon" viewBox="0 0 24 24" fill="#fff"><path d="M19.4 13a7.5 7.5 0 0 0 0-2l2.1-1.6-2-3.5-2.5 1a7 7 0 0 0-1.7-1L15 3.2h-4l-.4 2.7a7 7 0 0 0-1.7 1l-2.5-1-2 3.5L6.6 11a7.5 7.5 0 0 0 0 2l-2.1 1.6 2 3.5 2.5-1a7 7 0 0 0 1.7 1l.4 2.7h4l.4-2.7a7 7 0 0 0 1.7-1l2.5 1 2-3.5zM12 15.5A3.5 3.5 0 1 1 12 8.5a3.5 3.5 0 0 1 0 7z"/></svg>
      <h3>Internal Pivot Assessment &amp; Post Exploitation</h3>
      <p>We start as a low privileged users and attempted to move through the network in an attempt to access the data the matters to you. This is a simulation of a rogue trusted insider or a compromised internal host. We determine your risk when the egg shell is cracked. Even a seemingly insignificant compromise can have big consequences, and our goal is to demonstrate this risk.</p>
    </article>
    <article class="service">
      <svg class="service-icon" viewBox="0 0 24 24" fill="none" stroke="#fff" stroke-width="1.4"><rect x="5" y="3" width="14" height="13" rx="1"/><rect x="8" y="6" width="8" height="6"/><path d="M9 16v3h6v-3M7 21h10"/></svg>
      <h3>Advanced Product, Hardware &amp; RF Testing:</h3>
      <p>This a highly customized assessment designed for you and your hardware. Depending on the product we will analyze custom RF protocols, reverse engineer OS and firmware, and analyze and fuzz network protocols.<br>We have tested a range of products from toys to security products.</p>
    </article>
    <article class="service">
      <svg class="service-icon" viewBox="0 0 24 24" fill="none" stroke="#fff" stroke-width="1.4"><path d="M3 3h2v5M8 3h3v5H8zM14 3h2v5M18 3h3v5h-3zM3 11h3v5H3zM9 11h2v5"/><circle cx="16" cy="15" r="3.5"/><path d="M18.5 17.5L22 21"/></svg>
      <h3>Mobile Application Assessment</h3>
      <p>We look at your mobile application and the associated infrastructure to find configuration weaknesses, server-side issues, insecure authentication and access control, and other issues related to the latest attacks on mobile applications.</p>
    </article>
    <article class="service">
      <svg class="service-icon" viewBox="0 0 24 24" fill="#fff"><path d="M19.4 13a7.5 7.5 0 0 0 0-2l2.1-1.6-2-3.5-2.5 1a7 7 0 0 0-1.7-1L15 3.2h-4l-.4 2.7a7 7 0 0 0-1.7 1l-2.5-1-2 3.5L6.6 11a7.5 7.5 0 0 0 0 2l-2.1 1.6 2 3.5 2.5-1a7 7 0 0 0 1.7 1l.4 2.7h4l.4-2.7a7 7 0 0 0 1.7-1l2.5 1 2-3.5zM12 15.5A3.5 3.5 0 1 1 12 8.5a3.5 3.5 0 0 1 0 7z"/></svg>
      <h3>External Penetration Testing</h3>
      <p>This includes vulnerability scans of the public facing systems where we manually verify issues and exploit any issues found. We report on the issues that actually have a real risk to your organization.</p>
    </article>
    <article class="service">
      <svg class="service-icon" viewBox="0 0 24 24" fill="none" stroke="#fff" stroke-width="1.4"><rect x="5" y="3" width="14" height="13" rx="1"/><rect x="8" y="6" width="8" height="6"/><path d="M9 16v3h6v-3M7 21h10"/></svg>
      <h3>Internal Penetration Testing</h3>
      <p>This includes port scans and vulnerability scans of the internal network. We validate the results and look for issues that aren't found by scanners. We filter the issues and tell you the ones that matter most and represent the highest risk to your organization.</p>
    </article>
    <article class="service">
      <svg class="service-icon" viewBox="0 0 24 24" fill="none" stroke="#fff" stroke-width="1.4"><path d="M3 3h2v5M8 3h3v5H8zM14 3h2v5M18 3h3v5h-3zM3 11h3v5H3zM9 11h2v5"/><circle cx="16" cy="15" r="3.5"/><path d="M18.5 17.5L22 21"/></svg>
      <h3>Web Application Penetration Testing:</h3>
      <p>Our team will perform and in-depth analysis of your web application to find vulnerabilities related to programming errors, misconfiguration, and application architectural issues. We will perform automated and manual runtime analysis of your application. We create custom test cases to fuzz your application and find the faults before the bad guys do.</p>
    </article>
  </div>
</section>

<section class="about">
  <svg class="abs about-shade" viewBox="0 0 1200 510" preserveAspectRatio="none"><polygon points="620,0 1200,0 1200,510 980,510" fill="#2a2a2a"/><polygon points="760,0 1200,0 1200,300" fill="#3a3a3a"/></svg>
  <h2 class="abs section-title">About us</h2>
  <p class="abs about-text">Red Team Adversary Simulation - A goal based assessment where we attack just like a real world adversary.This includes external attacks and targeted phishing to demonstrate the real risk to your data.</p>
  <div class="abs device" role="img" aria-label="Laptop showing the Blue Harbor homepage with a play button for the company video"></div>
</section>

<section class="contact">
  <h2 class="abs section-title">Contact us</h2>
  <p class="abs contact-sub">For any question feel free<br>to conact us</p>
  <div class="abs field" style="left:472px;top:153px;width:302px">First name</div>
  <div class="abs field" style="left:823px;top:153px;width:302px">Last name</div>
  <div class="abs field" style="left:472px;top:256px;width:653px">Enter your email address</div>
  <div class="abs field" style="left:472px;top:358px;width:653px">Type your messahe hre</div>
  <div class="abs send">SEND</div>
</section>

<section class="testimonial">
  <div class="abs quote" style="left:235px">“</div>
  <div class="abs quote" style="left:820px">”</div>
  <div class="abs avatar" role="img" aria-label="Portrait photo of the client giving the testimonial"></div>
  <p class="abs cite">Dana Whitfield</p>
  <p class="abs quote-text">Lorem Ipsum is simply dummy text of the printing and typesetting industry. Lorem Ipsum has been the industry's standard dummy text ever since the 1500s, when an unknown printer took a galley of type and scrambled it to make a type specimen book.</p>
  <div class="abs arrow" style="left:0"><svg width="30" height="40" viewBox="0 0 30 40"><path d="M22 4L8 20l14 16" fill="none" stroke="#fff" stroke-width="5"/></svg></div>
  <div class="abs arrow" style="left:1114px"><svg width="30" height="40" viewBox="0 0 30 40"><path d="M8 4l14 16L8 36" fill="none" stroke="#fff" stroke-width="5"/></svg></div>
</section>

<footer class="site-footer">
  <div class="abs brand"><span class="brand-mark"></span>Blue Harbor</div>
  <p class="abs footer-tag"><span class="red">OFFENSIVE</span> SOLUTIONS FROM<br><span class="red">OFFENSIVE</span> MINDS</p>
  <p class="abs footer-text">We hack stuff. No joke, that is what we do, but we are the good guys</p>
  <h4 class="abs footer-head" style="left:531px;top:92px;font-weight:400">FOLLOW US</h4>
  <div class="abs social"><span></span><span></span><span></span><span></span></div>
  <div class="abs contact-line" style="top:230px"><svg width="32" height="26" viewBox="0 0 32 26"><rect width="32" height="26" rx="3" fill="#fff"/><path d="M4 6l12 9 12-9" fill="none" stroke="#0b0b0b" stroke-width="3"/></svg>hello@blueharbor.example</div>
  <div class="abs contact-line" style="top:282px"><svg width="32" height="32" viewBox="0 0 32 32"><rect width="32" height="32" rx="4" fill="#fff"/><path d="M10 7l4 5-2 3c1.5 3 3 4.5 5 5.5l3-2 5 4-2 3c-8-1-14-7-15-15z" fill="#0b0b0b"/></svg>555-014-2090</div>
  <h4 class="abs footer-head" style="left:863px;top:92px;font-weight:400">USEFUL <span class="red">LINKS</span></h4>
  <ul class="abs links"><li>HOME</li><li>ABOUT US</li><li>SERVICES</li><li>CONTACT US</li></ul>
  <div class="abs copyright">© Copyright-2017 blueharbor.example All rights reserved</div>
</footer>

</body>
</html>
```